BrookVale Care - Figma **Updated**

Below are the instructions for the website redesign project for BrookVale Care:
Website Design Review
• Color Scheme: Maintain the clean and professional Red and White color theme.
• Layout: Ensure the layout is straightforward and user-friendly.
• Typography: Use modern and easy-to-read font choices.
• Mobile Optimization: Ensure the website is fully optimized for mobile devices.
Design Requirements
• Clean, Minimalistic, and Responsive Design:
o The design should be clean, easy to navigate, and modern.
o The primary user base consists of seniors, so accessibility and simplicity are key.
• Location-Based Pages:
o Develop pages for each medical clinic and pharmacy location to provide a unique digital presence for each branch.
• Current Content:
o The current content is good but needs to be more efficient and user-friendly for patients.
• Doctor and Staff Introductions:
o Include an introduction section for our doctors and staff to build trust with visitors.
• Custom Design:
o Please avoid using ready-made themes. The preferred design source is a Figma file for development with Elementor.
• Logo:
o See the attached logo for reference.
Key Sections to Enhance
• My Team Section: Enhance this section to highlight healthcare professionals and build trust with visitors.
• Footer Section: Improve the footer by including more links to important sections and social media icons. Ensure the DosaTrak Logo is included on all footers.
• Contact Us Page: Enhance the Contact Us page to include options to upload documents and select specific locations or services.
• Intake Form Page: Improve the Intake Form page by implementing user-friendly and accessible forms.
• Patient Consent Forms: Implement patient consent forms for marketing purposes that are integrated with our database and software.
Websites for Design Inspiration
1. Pelvo Wellness: https://www.pelvowellness.example/?form=MG0AV3
• What We Like: The overall theme, font choices, and the look and feel of the website.
2. TabletNest: https://www.tabletnest.example/
• What We Like: The clean and intuitive layout.
3. Orvanta Care: https://orvantacare.example/
• What We Like: Everything about the design, including aesthetics, usability, and functionality.

Color and Theme Ideas
• Clinic Red, Pharmacy Green, Blue Branding:
o https://www.pelvowellness.example/?form=MG0AV3
o https://quorvix.example/
o https://www.kfl.example/en/financing?form=MG0AV3
o https://remotejourneycare.example/
Design Inspirations
• https://orvantacare.example/
• https://www.tabletnest.example/
• https://www.plinths.example/online/pharmacy/
• https://pharmacy.zentoro.example/
• https://www.dosecrate.example/how-it-works
• https://farcareqo.example/
Pages to Design
1. Landing Page (Clinic): https://brookvalecare.ca/
2. Medical Clinic Intake Instructions: https://brookvalecare.ca/medical-clinic-intake-form/
3. My Team Page and Introduction for Each Team Member
4. Book Appointment: https://brookvalecare.ca/book-appointment/
o Dropdown/Options on the page:
1. Family Practice
2. Walk-In Telehealth
3. Travel Consultation – Telehealth
4. Private Consult with Nurse Practitioner
5. Pharmacy: https://brookvalecare.ca/pharmacy/ (Pay attention to Pop-up Design)
6. Home Monitoring: https://brookvalecare.ca/home-monitoring-program/
7. Home Health Care: https://brookvalecare.ca/home-healthcare/
8. Contact Us: https://brookvalecare.ca/contact/
9. Resources: https://brookvalecare.ca/resources/ (We need Blog and News)
10. Blog Template: https://brookvalecare.ca/2025/02/14/find-doctor-surrey/ (Need massive improvement and responsiveness)
11. Join My Team: https://brookvalecare.ca/career/
Additional Improvements
• Header, Footer, and Banners: Massive improvement needed (Video integration would be great).
• Privacy Policy | Cookies | Terms and Conditions: Improvements needed.
Comments for Teodor
• Footer: We need a footer like TabletNest.
• Mobile Design: Ensure mobile design is similar to TabletNest.
• Social Media and Blogs: Integration needed.
• Email/Marketing List Sign-Up: Implement a sign-up option for patients/visitors.
• Reviewly Reviews: Integrate Reviewly reviews.
• Clinic Videos and Pictures: Include multimedia content.
• Keyword Optimization: Content will be rephrased for keyword optimization (keywords list provided).
• Keywords: I will ask that certain keywords [e.g. from blog] to link certain website page automatically
• DosaTrak Logo: Include DosaTrak logo at the bottom.
• Online Appointment Dropdown: Add dropdown options for different appointment types.
Please proceed with the necessary updates and preparations. Once you have the revised design ready in Figma, kindly send it over for approval.
We currently use the BrookVale Part with Vector and Tag line as the logo for both our Clinic and Pharmacy businesses. However, we have several design considerations and requests:

Banner Designs: What will each banner look like?

Other Pages: How will the other pages appear?

Header and Footer: The current designs for the header and footer are not satisfactory.

Text Placement and Font: We need improved text placement and a better font choice.

Team Members' Pictures: Use actual pictures of our team members.

Logos for Specific Services: Please update the logo/Vector for services such as Chronic Complex Care and Diagnostic Investigations.

Location-Based Pages: We need separate pages for the Pharmacy and Clinic, with links specific to each city—Surrey and White Rock.
Looking forward to seeing the improvements!

• design ready in Figma

```html
<!DOCTYPE html>
<html lang="en">
<head>
<meta charset="utf-8">
<title>BrookVale Care — Landing Page</title>
<link href="https://fonts.googleapis.com/css2?family=Outfit:ital,wght@0,400;0,500;0,600;0,700;0,800;1,400;1,500&display=swap" rel="stylesheet">
<style>
:root{
  --stage:#82111f;
  --navy:#2b3286;
  --red:#d71f36;
  --red-deep:#a8142a;
  --ink:#55586a;
  --muted:#8a8c99;
  --paper:#ffffff;
  --mist:#f3f3f4;
  --line:#e2e2e6;
}
*{box-sizing:border-box;margin:0;padding:0}
html,body{width:1033px;height:1200px;overflow:hidden}
body{background:var(--stage);font-family:"Outfit",sans-serif;color:var(--ink);position:relative}

.page{position:absolute;left:362px;top:0;width:984px;height:3826px;background:var(--paper);
  transform:scale(0.3137);transform-origin:0 0;overflow:hidden}
.abs{position:absolute}

/* header */
.site-header{left:0;top:0;width:984px;height:56px}
.brand{display:flex;align-items:center;gap:8px;font-weight:700;color:var(--navy);font-size:19px}
.brand .mark{width:14px;height:14px;background:var(--red);border-radius:3px}
.site-header .brand{position:absolute;left:46px;top:16px}
.main-nav{position:absolute;left:322px;top:22px;display:flex;gap:22px;font-size:10px;color:#333}
.btn-outline{position:absolute;left:850px;top:18px;width:90px;height:20px;border:1.5px solid var(--red);
  border-radius:4px;color:var(--red);font-size:9px;display:flex;align-items:center;justify-content:center}

/* hero */
.hero{left:50px;top:60px;width:882px;height:412px;border-radius:26px;overflow:hidden;
  background:linear-gradient(100deg,#eeeff1 0%,#dfe3e8 45%,#b9c6d4 70%,#d9d3cb 100%)}
.hero-card{left:130px;top:154px;width:362px;height:222px;background:var(--paper);border-radius:14px;padding:24px 38px}
.eyebrow{font-size:16px;letter-spacing:1.6px;color:#222;font-weight:500}
.hero-title{margin-top:14px;font-size:48px;line-height:49px;font-weight:800;color:var(--navy)}
.btn-red{display:inline-flex;align-items:center;justify-content:center;background:var(--red);color:#fff;
  font-weight:600;border-radius:4px}
.hero-card .btn-red{margin-top:12px;width:196px;height:28px;font-size:11px}

/* section headings */
.h2{font-size:27px;font-weight:800;color:var(--navy)}
.kicker{font-size:10px;font-style:italic;color:var(--red)}
.body-s{font-size:9.5px;line-height:14px;color:var(--ink)}
.arrow-btn{width:30px;height:20px;border:1.5px solid var(--red);border-radius:6px;display:flex;align-items:center;justify-content:center}

/* services */
.service-card{top:648px;width:204px;height:258px;border-radius:10px;overflow:hidden}
.service-card .photo{height:186px}
.service-card .band{height:72px;display:flex;justify-content:space-between;align-items:center;padding:0 18px;
  color:#fff;font-size:12.5px;font-weight:600;line-height:16px}
.band.red{background:var(--red)}
.band.navy{background:var(--navy)}

/* about */
.about-photo{left:54px;top:988px;width:316px;height:300px;border-radius:18px;
  background:linear-gradient(135deg,#c9cbd1,#6f6a70 55%,#2f2a2d)}
.about-copy{left:434px;top:1066px;width:470px}
.about-copy ul{margin:6px 0 0 14px;font-size:8.5px;line-height:12.5px}

/* mission */
.mission{left:54px;top:1366px;width:872px;height:142px;border-radius:22px;background:var(--navy);
  text-align:center;color:#fff;padding-top:38px}
.mission h3{font-size:25px;font-weight:700}
.mission p{margin:14px auto 0;width:600px;font-size:8.5px;line-height:13px;color:#dfe1f2}
.mission-icon{left:462px;top:1338px;width:60px;height:60px;border-radius:50%;background:#fff;border:3px solid var(--navy);
  display:flex;align-items:center;justify-content:center}

/* reviews */
.reviews{left:0;top:1610px;width:984px;height:452px;background:var(--mist)}
.review-card{width:206px;background:#fff;border-radius:6px;box-shadow:0 6px 16px rgba(0,0,0,.08);padding:16px 46px}
.stars{color:var(--red);font-size:13px;letter-spacing:3px}
.review-card p{margin-top:10px;font-size:8px;line-height:12px;color:var(--muted)}
.reviewer{margin-top:10px;font-size:11px;font-weight:700;color:var(--navy)}
.when{font-size:8px;font-style:italic;color:var(--red)}
.client-says{left:616px;top:1736px;width:280px}
.client-says h2{font-size:25px;line-height:30px;font-weight:700;color:var(--navy)}

/* team */
.team-band{left:0;top:2062px;width:984px;height:258px;background:var(--red)}
.team-title{left:0;top:2120px;width:984px;text-align:center;color:#fff}
.team-title h2{font-size:27px;font-weight:700}
.team-title p{font-size:9px;margin-top:10px}
.member{top:2212px;width:184px;text-align:center}
.member .photo{height:216px;border-radius:8px;position:relative}
.member .name{position:absolute;left:14px;right:14px;bottom:14px;height:26px;background:#fff;border-radius:4px;
  font-size:9px;font-weight:700;color:var(--navy);display:flex;align-items:center;justify-content:center}
.member .role{margin-top:16px;font-size:9px;line-height:13px;font-style:italic;color:var(--red)}

/* resources */
.divider{left:80px;top:2594px;width:822px;height:1px;background:var(--line)}
.res-head{left:0;top:2650px;width:984px;text-align:center}
.res-head p{font-size:9px;margin-top:8px;color:var(--ink)}
.post{top:2734px;width:258px}
.post .photo{height:256px;border-radius:14px;position:relative}
.post .date{position:absolute;left:30px;right:30px;bottom:22px;height:32px;background:#fff;border-radius:6px;
  font-size:8px;color:var(--red);padding:11px 24px}
.post h4{margin:24px 12px 0;font-size:12.5px;line-height:18px;font-weight:600;color:var(--navy)}
.post p{margin:12px 12px 0;font-size:8px;line-height:12px;color:var(--muted)}
.post .arrow-btn{margin:16px 12px 0}
.view-more{left:394px;top:3172px;width:194px;height:28px;font-size:11px}

/* footer */
.site-footer{left:0;top:3270px;width:984px;height:486px;background:linear-gradient(90deg,#a5162a,var(--red) 60%)}
.site-footer .brand{position:absolute;left:54px;top:78px;color:#fff}
.site-footer .brand .mark{background:#fff}
.foot-links{left:54px;top:128px;font-size:8.5px;line-height:14px;color:#fff;list-style:none}
.foot-col{top:72px;width:160px;color:#fff;font-size:8px;line-height:12px}
.foot-col .col-head{display:flex;gap:8px;align-items:flex-start;font-weight:600;font-size:8.5px;line-height:12px;margin-bottom:20px}
.foot-col .col-head i{flex:none;width:14px;height:14px;border:1.5px solid #fff;border-radius:3px}
.foot-col p{margin-bottom:14px}
.bottom-bar{left:0;top:3756px;width:984px;height:70px;background:#fff;font-size:8px;color:var(--muted)}
.bottom-bar .legal{position:absolute;left:54px;top:30px}
.bottom-bar .copy{position:absolute;left:372px;top:30px}
.bottom-bar .brand{position:absolute;left:820px;top:22px;font-size:16px;color:var(--navy);gap:6px}
.bottom-bar .brand .dot{width:16px;height:16px;border-radius:50%;border:2px solid var(--navy)}
</style>
</head>
<body>
<main class="page">

  <header class="site-header abs">
    <div class="brand"><span class="mark"></span>BrookVale</div>
    <nav class="main-nav">
      <span>Medical Clinic</span><span>Pharmacy</span><span>Home Monitoring</span><span>Home Healthcare</span><span>Contact Us</span><span>Resources</span>
    </nav>
    <span class="btn-outline">Book Appointment</span>
  </header>

  <section class="hero abs" role="img" aria-label="Nurse in blue scrubs reviewing a clipboard with a seated senior patient"></section>
  <div class="hero-card abs">
    <p class="eyebrow">Medical Clinic Intake Form</p>
    <h1 class="hero-title">Your Partner<br>In Health</h1>
    <span class="btn-red">Download Intake Forms</span>
  </div>

  <section>
    <h2 class="h2 abs" style="left:54px;top:524px">Our Services</h2>
    <p class="kicker abs" style="left:54px;top:564px">Convenient, Quality Care in Surrey and White Rock</p>
    <p class="body-s abs" style="left:54px;top:592px;width:740px">At our walk-in clinic and medical clinic in Surrey and White Rock, we offer a wide range of healthcare services to meet the diverse needs of our community. Whether you're looking for urgent care, routine check-ups, or specialized treatment, we provide accessible, affordable healthcare in Surrey and White Rock.</p>
    <div class="abs" style="left:862px;top:576px;display:flex;gap:10px">
      <span class="arrow-btn"><svg width="14" height="10" viewBox="0 0 14 10"><path d="M13 5H1M5 1 1 5l4 4" fill="none" stroke="#d71f36" stroke-width="1.5"/></svg></span>
      <span class="arrow-btn"><svg width="14" height="10" viewBox="0 0 14 10"><path d="M1 5h12M9 1l4 4-4 4" fill="none" stroke="#d71f36" stroke-width="1.5"/></svg></span>
    </div>

    <article class="service-card abs" style="left:52px">
      <div class="photo" role="img" aria-label="Hands holding a patient's hand in care" style="background:linear-gradient(135deg,#5b7fa0,#c98f7a 60%,#e9cbb8)"></div>
      <div class="band red"><span>Chronic and Complex<br>Care</span><svg width="12" height="8" viewBox="0 0 14 10"><path d="M1 5h12M9 1l4 4-4 4" fill="none" stroke="#fff" stroke-width="1.5"/></svg></div>
    </article>
    <article class="service-card abs" style="left:274px">
      <div class="photo" role="img" aria-label="Laboratory glassware on a bench" style="background:linear-gradient(160deg,#f2f3f5,#9aa2ad 60%,#5c636e)"></div>
      <div class="band navy"><span>Diagnostic<br>Investigation</span><svg width="12" height="8" viewBox="0 0 14 10"><path d="M1 5h12M9 1l4 4-4 4" fill="none" stroke="#fff" stroke-width="1.5"/></svg></div>
    </article>
    <article class="service-card abs" style="left:495px">
      <div class="photo" role="img" aria-label="Smiling family with young children" style="background:linear-gradient(160deg,#dfe6ee,#c9a890 55%,#6b5a4f)"></div>
      <div class="band red"><span>Full Family Care<br>Services</span><svg width="12" height="8" viewBox="0 0 14 10"><path d="M1 5h12M9 1l4 4-4 4" fill="none" stroke="#fff" stroke-width="1.5"/></svg></div>
    </article>
    <article class="service-card abs" style="left:716px">
      <div class="photo" role="img" aria-label="Open binder of claim documents" style="background:linear-gradient(160deg,#d98a3a,#c9c2b5 50%,#8f8a84)"></div>
      <div class="band navy"><span>WSB and RAIC<br>Claims</span><svg width="12" height="8" viewBox="0 0 14 10"><path d="M1 5h12M9 1l4 4-4 4" fill="none" stroke="#fff" stroke-width="1.5"/></svg></div>
    </article>
    <article class="service-card abs" style="left:937px">
      <div class="photo" role="img" aria-label="Screening exam equipment" style="background:linear-gradient(160deg,#e3ddd2,#b48a4e)"></div>
      <div class="band red"><span>Screening<br>Exams</span></div>
    </article>
  </section>

  <section>
    <div class="about-photo abs" role="img" aria-label="Doctor listening through a stethoscope"></div>
    <div class="about-copy abs">
      <h2 class="h2" style="font-size:25px">About Us</h2>
      <p class="kicker" style="margin-top:10px;font-size:9px">We're an established, forward-thinking family practice in White Rock/South Surrey.</p>
      <p class="body-s" style="margin-top:12px;font-size:8.5px;line-height:12.5px">We're proud to provide top-notch healthcare services at BrookVale in White Rock.</p>
      <ul>
        <li>We are a trusted family doctor in White Rock and Surrey, committed to offering reliable family doctors in Surrey with a focus on providing convenient medical care in Surrey. Our medical clinic, Surrey and walk-in clinic Surrey are equipped with the latest technology and a skilled team to ensure exceptional care in a safe and supportive environment.</li>
      </ul>
    </div>
  </section>

  <section>
    <div class="mission abs">
      <h3>Mission Statement</h3>
      <p>Our mission is to be the best walk-in clinic in Surrey and a top-rated medical clinic in Surrey, leading the way in innovation and patient care. We aim to provide affordable healthcare in Surrey that is empathetic, efficient, and accessible to all.</p>
    </div>
    <div class="mission-icon abs">
      <svg width="30" height="30" viewBox="0 0 30 30" fill="none" stroke="#d71f36" stroke-width="2"><circle cx="15" cy="15" r="11"/><circle cx="15" cy="15" r="6"/><circle cx="15" cy="15" r="1.5" fill="#d71f36"/><path d="M15 15 24 6M21 6h3v3"/></svg>
    </div>
  </section>

  <section>
    <div class="reviews abs"></div>
    <article class="review-card abs" style="left:82px;top:1590px">
      <div class="stars">★★★★★</div>
      <p>Very good experience, the doctor was very kind and was able to clarify all my doubts. Thank you very much!</p>
      <div class="reviewer">Maren Oakley</div><div class="when">7 days ago</div>
    </article>
    <article class="review-card abs" style="left:324px;top:1660px">
      <div class="stars">★★★★★</div>
      <p>Very good experience, the doctor was very kind and was able to clarify all my doubts. Thank you very much!</p>
      <div class="reviewer">Maren Oakley</div><div class="when">7 days ago</div>
    </article>
    <article class="review-card abs" style="left:82px;top:1816px">
      <div class="stars">★★★★★</div>
      <p>Very good experience, the doctor was very kind and was able to clarify all my doubts. Thank you very much!</p>
      <div class="reviewer">Maren Oakley</div><div class="when">7 days ago</div>
    </article>
    <article class="review-card abs" style="left:324px;top:1894px">
      <div class="stars">★★★★★</div>
      <p>Very good experience, the doctor was very kind and was able to clarify all my doubts. Thank you very much!</p>
      <div class="reviewer">Maren Oakley</div><div class="when">7 days ago</div>
    </article>
    <div class="client-says abs">
      <h2>What our client says<br>about us</h2>
      <div class="brand" style="margin-top:22px;font-size:15px"><span class="mark" style="width:11px;height:11px"></span>BrookVale</div>
      <div style="margin-top:12px;display:flex;gap:12px;align-items:center"><span class="stars">★★★★★</span><span style="color:var(--red);font-style:italic;font-size:13px">4.9</span></div>
      <p style="margin-top:10px;font-size:7.5px;color:var(--muted)">Based on 159 reviews</p>
      <p style="margin-top:16px;font-size:11px;color:var(--muted)">powered by Reviewly</p>
    </div>
  </section>

  <section>
    <div class="team-band abs"></div>
    <div class="team-title abs"><h2>Our Team</h2><p>Healing minds with compassionate hearts</p></div>
    <article class="member abs" style="left:0;width:170px">
      <div class="photo" role="img" aria-label="Portrait of team member" style="background:linear-gradient(160deg,#e9c9a0,#6a4a34)"><span class="name">Dr. Ilse R Varnham</span></div>
      <p class="role">Occupational Therapist,<br>Inclusion Health</p>
    </article>
    <article class="member abs" style="left:192px">
      <div class="photo" role="img" aria-label="Portrait of team member" style="background:linear-gradient(160deg,#f1efeb,#b9a48e)"><span class="name">Dr. Ilse R Varnham</span></div>
      <p class="role">Occupational Therapist,<br>Inclusion Health</p>
    </article>
    <article class="member abs" style="left:398px">
      <div class="photo" role="img" aria-label="Portrait of team member" style="background:linear-gradient(160deg,#c9cdd3,#4d3a30)"><span class="name">Dr. Ilse R Varnham</span></div>
      <p class="role">Occupational Therapist,<br>Inclusion Health</p>
    </article>
    <article class="member abs" style="left:606px">
      <div class="photo" role="img" aria-label="Portrait of team member" style="background:linear-gradient(160deg,#9a6a58,#d21f34 70%)"><span class="name">Dr. Ilse R Varnham</span></div>
      <p class="role">Occupational Therapist,<br>Inclusion Health</p>
    </article>
    <article class="member abs" style="left:812px;width:172px">
      <div class="photo" role="img" aria-label="Portrait of team member" style="background:linear-gradient(160deg,#f4f4f4,#8d8f96)"><span class="name">Dr. Ilse R Varnham</span></div>
      <p class="role">Occupational Therapist,<br>Inclusion Health</p>
    </article>
    <div class="abs" style="left:456px;top:2504px;display:flex;gap:10px">
      <span class="arrow-btn"><svg width="14" height="10" viewBox="0 0 14 10"><path d="M13 5H1M5 1 1 5l4 4" fill="none" stroke="#d71f36" stroke-width="1.5"/></svg></span>
      <span class="arrow-btn"><svg width="14" height="10" viewBox="0 0 14 10"><path d="M1 5h12M9 1l4 4-4 4" fill="none" stroke="#d71f36" stroke-width="1.5"/></svg></span>
    </div>
  </section>

  <div class="divider abs"></div>

  <section>
    <div class="res-head abs"><h2 class="h2" style="font-weight:700">Resources</h2><p>Explore the latest news and resources</p></div>
    <article class="post abs" style="left:80px">
      <div class="photo" role="img" aria-label="Hands writing notes beside a laptop" style="background:linear-gradient(150deg,#f1f2f4,#c9d0d8 60%,#8e99a6)"><span class="date">Feb 14, 2025</span></div>
      <h4>What to Do If You Don't Have a Family Doctor in White Rock, South Surrey, and Surrey</h4>
      <p>Finding a family doctor in White Rock, South Surrey, or Surrey can be challenging...</p>
      <span class="arrow-btn"><svg width="14" height="10" viewBox="0 0 14 10"><path d="M1 5h12M9 1l4 4-4 4" fill="none" stroke="#d71f36" stroke-width="1.5"/></svg></span>
    </article>
    <article class="post abs" style="left:362px">
      <div class="photo" role="img" aria-label="Doctor holding a stethoscope shaped like a heart" style="background:linear-gradient(150deg,#3a5f8f,#1e3350 55%,#d9334a)"><span class="date">Feb 14, 2025</span></div>
      <h4>What to Do If You Don't Have a Family Doctor in White Rock, South Surrey, and Surrey</h4>
      <p>Finding a family doctor in White Rock, South Surrey, or Surrey can be challenging...</p>
      <span class="arrow-btn"><svg width="14" height="10" viewBox="0 0 14 10"><path d="M1 5h12M9 1l4 4-4 4" fill="none" stroke="#d71f36" stroke-width="1.5"/></svg></span>
    </article>
    <article class="post abs" style="left:644px">
      <div class="photo" role="img" aria-label="Doctor in a white coat with a stethoscope" style="background:linear-gradient(150deg,#eef1f5,#b8c6d6 60%,#7d8ea3)"><span class="date">Feb 14, 2025</span></div>
      <h4>What to Do If You Don't Have a Family Doctor in White Rock, South Surrey, and Surrey</h4>
      <p>Finding a family doctor in White Rock, South Surrey, or Surrey can be challenging...</p>
      <span class="arrow-btn"><svg width="14" height="10" viewBox="0 0 14 10"><path d="M1 5h12M9 1l4 4-4 4" fill="none" stroke="#d71f36" stroke-width="1.5"/></svg></span>
    </article>
    <span class="btn-red view-more abs">View More Resources</span>
  </section>

  <footer>
    <div class="site-footer abs">
      <div class="brand"><span class="mark"></span>BrookVale</div>
      <ul class="foot-links abs">
        <li>Medical Clinic</li><li>Pharmacy</li><li>Home Monitoring</li><li>Home Healthcare</li><li>Contact Us</li><li>Resources</li><li>Join Our Team</li>
      </ul>
      <div class="foot-col abs" style="left:278px">
        <div class="col-head"><i></i><span>BrookVale Medical<br>Clinic – White Rock</span></div>
        <p>12-2207 Alder Row<br>White Rock, BC V0X 1A1</p>
        <p>Monday – Friday<br>09:00 AM – 05:00 PM</p>
        <p>Saturday, Sunday and Statutory<br>Holiday – Closed</p>
        <p>Online Services<br>Monday to Sunday<br>09:00 AM – 05:30 PM</p>
        <p>info@brookvalecare.ca</p>
        <p>Phone: +1 (604) 555-0143</p>
        <p>Fax: +1 (604) 555-0142</p>
      </div>
      <div class="foot-col abs" style="left:452px">
        <div class="col-head"><i></i><span>BrookVale Pharmacy<br>– White Rock</span></div>
        <p>12-2207 Alder Row<br>White Rock, BC V0X 1A1</p>
        <p>Monday – Friday<br>09:00 AM – 06:30 PM</p>
        <p>Saturday – 10:00 AM – 03:30 PM</p>
        <p>Sunday and Statutory Holiday<br>10:00 AM – 02:00 PM</p>
        <p>We offer Free Delivery<br>Weekdays – Same Day Free<br>Delivery (On orders before 04:00 PM)<br>Weekends – Next Day Free<br>Delivery</p>
        <p>rx@brookvalecare.ca</p>
        <p>Phone: +1 (604) 555-0190</p>
        <p>Fax: +1 (604) 555-0191</p>
      </div>
      <div class="foot-col abs" style="left:632px">
        <div class="col-head"><i></i><span>BrookVale Medical<br>Clinic – Surrey</span></div>
        <p>#210 8840 Cedar Lane<br>Surrey, BC V0X 2B2</p>
        <p>Monday – Friday<br>9:00AM – 6:30PM</p>
        <p>medical@brookvalecare.ca</p>
        <p>Phone: +1 (604) 555-0166</p>
        <p>Fax: +1 (604) 555-0167</p>
      </div>
      <div class="foot-col abs" style="left:800px">
        <div class="col-head"><i></i><span>BrookVale Pharmacy<br>– Surrey</span></div>
        <p>#214 8840 Cedar Lane<br>Surrey, BC V0X 2B2</p>
        <p>Monday – Friday<br>9:00AM – 6:30PM</p>
        <p>pharmacy@brookvalecare.ca</p>
        <p>Phone: +1 (604) 555-0186</p>
        <p>Fax: +1 (604) 555-0185</p>
      </div>
    </div>
    <div class="bottom-bar abs">
      <span class="legal">Privacy Policy | Cookies | Terms and Conditions</span>
      <span class="copy">Copyright © 2025 BrookVale Medical All rights reserved</span>
      <div class="brand"><span class="dot"></span>DosaTrak</div>
    </div>
  </footer>

</main>
</body>
</html>
```